I need to refresh my meeting minutes pages (2 of them)

I have 2 pages that need to be modernized with a new look and feel. I have attached the 2 pages that need the refresh. I am okay with one page submissions as long as the winner is willing to add the second page before payment :-) Any questions please let me know. The logo on the page is not ours but a sample of what client may give us.

```html
<!DOCTYPE html>
<html lang="en">
<head>
<meta charset="utf-8">
<title>Meetings – Regular Meeting Agenda</title>
<link rel="stylesheet" href="https://fonts.googleapis.com/css2?family=Figtree:wght@400;500;600;700;800&display=swap">
<style>
  :root {
    --blue: #0777bd;
    --ink: #111111;
    --text: #4a4a4a;
    --panel: #f7f7f7;
    --white: #ffffff;
    --star: #f0a020;
    --cancel: #e52420;
    --muted-btn: #f1f1f1;
  }
  * { box-sizing: border-box; margin: 0; padding: 0; }
  html, body {
    width: 1200px; height: 800px; overflow: hidden;
    background: var(--white);
    font-family: "Figtree", sans-serif;
    color: var(--ink);
  }
  body { position: relative; }
  .site-header {
    position: absolute; left: 0; top: 0; width: 1200px; height: 83px;
    background: var(--white);
    box-shadow: 0 6px 16px rgba(7, 119, 189, 0.05);
    z-index: 2;
  }
  .brand {
    position: absolute; left: 25px; top: 20px;
    font-size: 38px; font-weight: 800; color: var(--blue);
    letter-spacing: -0.5px; line-height: 40px;
  }
  .main-nav { position: absolute; top: 25px; left: 0; width: 1200px; height: 34px; }
  .main-nav a {
    position: absolute; top: 0; height: 34px; line-height: 34px;
    font-size: 15px; font-weight: 700; color: var(--ink); text-decoration: none;
    white-space: nowrap;
  }
  .main-nav .nav-featured { left: 805px; }
  .main-nav .nav-meetings {
    left: 891px; width: 96px; text-align: center;
    background: var(--blue); color: var(--white); border-radius: 17px;
  }
  .main-nav .nav-agenda { left: 1012px; }
  .main-nav .nav-policies { left: 1106px; }

  .sidebar {
    position: absolute; left: 0; top: 83px; width: 392px; height: 717px;
    background: var(--panel); overflow: hidden;
  }
  .search-box {
    position: absolute; left: 25px; top: 25px; width: 342px; height: 47px;
    background: var(--white); border-radius: 6px;
    display: flex; align-items: center; padding-left: 17px; gap: 10px;
    font-size: 14.5px; color: var(--text);
  }
  .filter {
    position: absolute; left: 25px; width: 342px; height: 43px; border-radius: 6px;
    display: flex; align-items: center; justify-content: space-between;
    padding: 0 17px; font-size: 14.5px; font-weight: 700;
  }
  .filter-featured { top: 85px; background: var(--white); color: var(--ink); }
  .filter-year {
    top: 141px; background: var(--blue); color: var(--white);
    box-shadow: 0 8px 18px rgba(7, 119, 189, 0.25);
  }
  .meeting-list { position: absolute; left: 25px; top: 190px; width: 342px; list-style: none; }
  .meeting-item {
    position: relative; height: 68px; padding: 10px 17px 0; white-space: nowrap;
  }
  .meeting-item.current {
    background: var(--white); border-radius: 6px; height: 63px; margin-bottom: 5px;
    padding-top: 11px;
    box-shadow: 0 4px 14px rgba(0,0,0,0.04);
  }
  .meeting-date { font-size: 14.5px; font-weight: 700; line-height: 20px; }
  .meeting-type { font-size: 14.5px; color: var(--text); line-height: 20px; }
  .current .meeting-date { color: var(--blue); }
  .canceled .meeting-date { color: var(--cancel); }
  .flag-star { position: absolute; right: 17px; top: 20px; }
  .flag-canceled {
    position: absolute; right: 17px; top: 20px; font-size: 14.5px; color: var(--cancel);
  }

  .pager {
    position: absolute; top: 108px; height: 37px; background: var(--muted-btn);
    border-radius: 6px; display: flex; align-items: center;
    font-size: 14.5px; font-weight: 700; white-space: nowrap;
  }
  .pager-prev { left: 417px; width: 145px; padding-left: 21px; gap: 14px; }
  .pager-next { left: 1036px; width: 139px; padding-left: 17px; gap: 14px; }

  .meeting-detail {
    position: absolute; left: 417px; top: 170px; width: 758px; height: 366px;
    background: var(--panel); padding: 24px 25px; overflow: hidden;
  }
  .meeting-detail h1 { font-size: 29px; font-weight: 700; line-height: 38px; white-space: nowrap; }
  .detail-date { font-size: 14.5px; font-weight: 700; color: var(--blue); margin-top: 8px; line-height: 20px; }
  .detail-label { font-size: 14.5px; font-weight: 700; color: var(--text); margin-top: 10px; line-height: 20px; }
  .detail-text { font-size: 14.5px; color: var(--text); line-height: 23.3px; margin-top: 2px; }
  .detail-gap { margin-top: 12px; }

  .actions { position: absolute; left: 417px; top: 561px; display: flex; gap: 9px; }
  .action-btn {
    height: 37px; background: var(--blue); color: var(--white); border-radius: 4px;
    display: flex; align-items: center; gap: 10px; padding: 0 17px;
    font-size: 14.5px; font-weight: 700; white-space: nowrap;
  }
</style>
</head>
<body>
  <header class="site-header">
    <div class="brand">NVSD</div>
    <nav class="main-nav">
      <a class="nav-featured" href="#">Featured</a>
      <a class="nav-meetings" href="#">Meetings</a>
      <a class="nav-agenda" href="#">Agenda</a>
      <a class="nav-policies" href="#">Policies</a>
    </nav>
  </header>

  <aside class="sidebar">
    <div class="search-box">
      <svg width="20" height="20" viewBox="0 0 20 20" fill="none" stroke="#4a4a4a" stroke-width="1.4"><circle cx="9" cy="9" r="8"/><path d="M15 15l2 2"/></svg>
      <span>Search for a Meeting</span>
    </div>
    <div class="filter filter-featured">
      <span>Featured</span>
      <svg width="16" height="10" viewBox="0 0 16 10" fill="none" stroke="#111" stroke-width="1.6"><path d="M1 1l7 7 7-7"/></svg>
    </div>
    <div class="filter filter-year">
      <span>2025</span>
      <svg width="16" height="10" viewBox="0 0 16 10" fill="none" stroke="#fff" stroke-width="1.6"><path d="M1 9l7-7 7 7"/></svg>
    </div>
    <ul class="meeting-list">
      <li class="meeting-item">
        <div class="meeting-date">May 1, 2025 (Thursday)</div>
        <div class="meeting-type">Special Meeting Agenda</div>
        <svg class="flag-star" width="18" height="18" viewBox="0 0 24 24"><path fill="var(--star)" d="M12 2l2.9 6.6 7.1.6-5.4 4.7 1.6 7-6.2-3.7-6.2 3.7 1.6-7L2 9.2l7.1-.6z"/></svg>
      </li>
      <li class="meeting-item current">
        <div class="meeting-date">Apr 24, 2025 (Thursday)</div>
        <div class="meeting-type">Regular Meeting Agenda</div>
      </li>
      <li class="meeting-item">
        <div class="meeting-date">Apr 10, 2025 (Thursday)</div>
        <div class="meeting-type">Regular Meeting Agenda</div>
      </li>
      <li class="meeting-item">
        <div class="meeting-date">Mar 20, 2025 (Thursday)</div>
        <div class="meeting-type">Regular Meeting Agenda</div>
      </li>
      <li class="meeting-item">
        <div class="meeting-date">Mar 17, 2025 (Monday)</div>
        <div class="meeting-type">Regular Meeting Agenda</div>
      </li>
      <li class="meeting-item">
        <div class="meeting-date">Mar 12, 2025 (Wednesday)</div>
        <div class="meeting-type">Special Meeting Agenda</div>
      </li>
      <li class="meeting-item">
        <div class="meeting-date">Mar 6, 2025 (Thursday)</div>
        <div class="meeting-type">Regular Meeting Agenda</div>
      </li>
      <li class="meeting-item canceled">
        <div class="meeting-date">Feb 26, 2025 (Thursday)</div>
        <div class="meeting-type">Special Meeting Agenda</div>
        <span class="flag-canceled">Canceled</span>
      </li>
    </ul>
  </aside>

  <div class="pager pager-prev">
    <svg width="9" height="16" viewBox="0 0 9 16" fill="none" stroke="#111" stroke-width="1.6"><path d="M8 1L1 8l7 7"/></svg>
    <span>Apr 10, 2025</span>
  </div>
  <div class="pager pager-next">
    <span>May 1, 2025</span>
    <svg width="9" height="16" viewBox="0 0 9 16" fill="none" stroke="#111" stroke-width="1.6"><path d="M1 1l7 7-7 7"/></svg>
  </div>

  <section class="meeting-detail">
    <h1>Regular Meeting Agenda</h1>
    <p class="detail-date">Thursday, April 24, 2025</p>
    <p class="detail-label">Location</p>
    <p class="detail-text">Linden Park High School Media Center<br>418 North Maple Grove Road<br>Ashford, Ohio 44290<br>6:00 P.M.</p>
    <p class="detail-label detail-gap">Time</p>
    <p class="detail-text">6:00 P.M.</p>
    <p class="detail-label detail-gap">Description</p>
    <p class="detail-text">This meeting is a meeting of the Board of Education in public for the purpose of conducting the District’s business. There is a time for public participation during the meeting as indicated in the agenda.</p>
  </section>

  <div class="actions">
    <div class="action-btn">
      <svg width="18" height="18" viewBox="0 0 20 20" fill="none" stroke="#fff" stroke-width="1.4"><rect x="3" y="3" width="14" height="15" rx="3"/><path d="M7 1.5v3M13 1.5v3M6.5 9h7M6.5 12.5h5"/></svg>
      <span>View Agenda</span>
    </div>
    <div class="action-btn">
      <svg width="18" height="18" viewBox="0 0 20 20" fill="none" stroke="#fff" stroke-width="1.4"><path d="M5 2h7l5 5v9a2 2 0 0 1-2 2H5a2 2 0 0 1-2-2V4a2 2 0 0 1 2-2z"/><path d="M10 8v6M7.5 11.5L10 14l2.5-2.5"/></svg>
      <span>Download PDF</span>
    </div>
    <div class="action-btn">
      <svg width="18" height="18" viewBox="0 0 20 20" fill="none" stroke="#fff" stroke-width="1.4"><rect x="6" y="2" width="8" height="5" rx="1"/><rect x="2.5" y="7" width="15" height="7" rx="2"/><rect x="6" y="12" width="8" height="6" rx="1"/></svg>
      <span>Print Agenda</span>
    </div>
    <div class="action-btn">
      <svg width="18" height="18" viewBox="0 0 20 20" fill="none" stroke="#fff" stroke-width="1.4"><path d="M18 2L2 8l6 3 3 6z"/><path d="M8 11l10-9"/></svg>
      <span>Share Agenda</span>
    </div>
  </div>
</body>
</html>
```